Casa Vantora
Stationery / Business Cards
Professional
Ramiro Quesada
Engineering
427 Brisadores
Suite 392
Laredo, TX
USA
1-800 597-RNQZ
ramiro@casavantora.com.mx
www.casavantora.com.mx
Logo & Website on background
"Control de Iluminacion
Audio y Video Distribuido
Home Theater
Telefonia, Voz y Datos
Integracion de Sistemas
Circuito Cerrado de TV
Ingenieria y Diseno"

```html
<!DOCTYPE html>
<html lang="es">
<head>
<meta charset="utf-8">
<title>Casa Vantora — Stationery</title>
<link href="https://fonts.googleapis.com/css2?family=Montserrat:wght@800&family=Open+Sans:wght@400;600&display=swap" rel="stylesheet">
<style>
:root{
  --blue:#1d63b0;
  --blue-dark:#0c3c78;
  --ink:#2b2f36;
  --grey:#8a9099;
  --paper:#ffffff;
  --stage:#e9eaec;
  --smoke:#cfd2d6;
}
*{box-sizing:border-box;margin:0;padding:0}
html,body{width:1200px;height:497px;overflow:hidden;background:var(--stage);font-family:"Open Sans",sans-serif;color:var(--ink)}
.canvas{position:relative;width:1200px;height:497px}
.piece{position:absolute;background:var(--paper);overflow:hidden;box-shadow:0 2px 6px rgba(0,0,0,.18)}
.piece svg.bg{position:absolute;inset:0;width:100%;height:100%}
.brand{position:absolute;display:flex;align-items:center;gap:5px}
.brand .dot{width:14px;height:14px;border-radius:50%;background:var(--blue)}
.brand .name{font-family:"Montserrat",sans-serif;font-weight:800;font-size:10px;color:var(--blue-dark);letter-spacing:.3px;line-height:1}
.tagline{position:absolute;font-size:4.5px;color:var(--grey)}
.person{position:absolute;text-align:right}
.person .nm{font-size:7px;font-weight:600;color:var(--blue-dark)}
.person .role{font-size:4.5px;color:var(--grey)}
.contact{position:absolute;font-size:4.2px;line-height:6px;color:var(--ink)}
.services{position:absolute;list-style:none;font-size:4.5px;line-height:7.2px}
.services li{display:flex;align-items:center;gap:3px}
.services li::before{content:"";width:3px;height:3px;border-radius:50%;background:var(--blue)}
.web{position:absolute;font-size:4.5px;font-weight:600}
.ring{position:absolute;border-radius:50%}
/* positions */
.card-front-a{left:14px;top:70px;width:192px;height:91px}
.card-front-b{left:214px;top:70px;width:192px;height:91px}
.card-back-light{left:14px;top:172px;width:192px;height:91px}
.card-back-blue{left:214px;top:172px;width:192px;height:91px;background:var(--blue)}
.card-back-smoke{left:108px;top:280px;width:184px;height:96px;background:var(--smoke)}
.letterhead{left:432px;top:30px;width:204px;height:300px}
.envelope-flap{left:700px;top:30px;width:476px;height:130px}
.envelope-plain{left:700px;top:175px;width:476px;height:130px}
.envelope-wave{left:700px;top:320px;width:340px;height:150px}
</style>
</head>
<body>
<main class="canvas">

  <!-- Business card front, side swoosh -->
  <section class="piece card-front-a">
    <svg class="bg" viewBox="0 0 192 91" preserveAspectRatio="none"><path d="M120 0 C100 35 150 60 130 91 L192 91 L192 0Z" fill="var(--blue)"/><path d="M112 0 C92 35 142 60 122 91" stroke="var(--blue-dark)" stroke-width="2" fill="none"/></svg>
    <div class="brand" style="left:8px;top:12px"><span class="dot"></span><span class="name">CASA<br>VANTORA</span></div>
    <div class="tagline" style="left:27px;top:35px">Smart Living Solutions</div>
    <div class="person" style="right:8px;top:8px;color:#fff"><div class="nm" style="color:#fff">Ramiro Quesada</div><div class="role" style="color:#dfe8f4">Engineering</div></div>
    <div class="contact" style="left:10px;bottom:8px">427 Brisadores, Suite 392<br>Laredo, TX USA<br>1-800 597-RNQZ<br>ramiro@casavantora.com.mx</div>
  </section>

  <!-- Business card front, bottom wave -->
  <section class="piece card-front-b">
    <svg class="bg" viewBox="0 0 192 91" preserveAspectRatio="none"><path d="M0 70 C60 40 120 95 192 50 L192 91 L0 91Z" fill="var(--blue)"/></svg>
    <div class="brand" style="left:8px;top:10px"><span class="dot"></span><span class="name">CASA<br>VANTORA</span></div>
    <div class="tagline" style="left:27px;top:33px">Smart Living Solutions</div>
    <div class="person" style="right:8px;top:8px"><div class="nm">Ramiro Quesada</div><div class="role">Engineering</div></div>
    <div class="contact" style="right:8px;top:30px;text-align:right">427 Brisadores, Suite 392<br>Laredo, TX USA<br>1-800 597-RNQZ<br>ramiro@casavantora.com.mx</div>
  </section>

  <!-- Business card back, light -->
  <section class="piece card-back-light">
    <svg class="bg" viewBox="0 0 192 91" preserveAspectRatio="none"><path d="M140 0 C120 40 160 60 150 91 L192 91 L192 0Z" fill="var(--blue)"/></svg>
    <div class="ring" style="left:12px;top:14px;width:40px;height:40px;background:var(--blue-dark)"></div>
    <ul class="services" style="left:64px;top:10px">
      <li>Control de Iluminacion</li><li>Audio y Video Distribuido</li><li>Home Theater</li><li>Telefonia, Voz y Datos</li><li>Integracion de Sistemas</li><li>Circuito Cerrado de TV</li><li>Ingenieria y Diseno</li>
    </ul>
    <div class="web" style="left:10px;bottom:5px;color:var(--blue-dark)">www.casavantora.com.mx</div>
  </section>

  <!-- Business card back, blue -->
  <section class="piece card-back-blue">
    <svg class="bg" viewBox="0 0 192 91" preserveAspectRatio="none"><path d="M0 0 L60 0 C45 40 75 60 55 91 L0 91Z" fill="var(--blue-dark)"/></svg>
    <div class="ring" style="left:12px;top:22px;width:40px;height:40px;background:#fff"></div>
    <ul class="services" style="left:80px;top:10px;color:#fff">
      <li>Control de Iluminacion</li><li>Audio y Video Distribuido</li><li>Home Theater</li><li>Telefonia, Voz y Datos</li><li>Integracion de Sistemas</li><li>Circuito Cerrado de TV</li><li>Ingenieria y Diseno</li>
    </ul>
  </section>

  <!-- Business card back, smoke -->
  <section class="piece card-back-smoke">
    <div class="ring" style="left:12px;top:16px;width:46px;height:46px;background:#1c1f24"></div>
    <ul class="services" style="left:76px;top:10px">
      <li>Control de Iluminacion</li><li>Audio y Video Distribuido</li><li>Home Theater</li><li>Telefonia, Voz y Datos</li><li>Integracion de Sistemas</li><li>Circuito Cerrado de TV</li><li>Ingenieria y Diseno</li>
    </ul>
    <div class="web" style="left:12px;bottom:6px;color:#1c1f24">www.casavantora.com.mx</div>
  </section>

  <!-- Letterhead -->
  <section class="piece letterhead">
    <svg class="bg" viewBox="0 0 204 300" preserveAspectRatio="none"><path d="M0 262 C60 230 130 290 204 245 L204 300 L0 300Z" fill="var(--blue)"/><path d="M0 255 C60 222 130 282 204 238" stroke="var(--blue-dark)" stroke-width="2" fill="none"/></svg>
    <div class="brand" style="left:12px;top:14px"><span class="dot"></span><span class="name">CASA<br>VANTORA</span></div>
    <div class="tagline" style="left:31px;top:37px">Smart Living Solutions</div>
    <div class="contact" style="left:118px;top:14px">427 Brisadores<br>Suite 392<br>Laredo, TX USA<br>1-800 597-RNQZ<br>ramiro@casavantora.com.mx<br>www.casavantora.com.mx</div>
    <div class="ring" style="left:72px;top:120px;width:60px;height:60px;background:var(--blue);opacity:.08"></div>
  </section>

  <!-- Envelope, grey flap -->
  <section class="piece envelope-flap">
    <svg class="bg" viewBox="0 0 476 130" preserveAspectRatio="none"><path d="M0 0 L476 0 L238 62Z" fill="#6d7278"/></svg>
    <div class="ring" style="left:226px;top:32px;width:24px;height:24px;background:#fff"></div>
  </section>

  <!-- Envelope, plain front -->
  <section class="piece envelope-plain">
    <div class="brand" style="left:16px;top:14px"><span class="dot"></span><span class="name">CASA<br>VANTORA</span></div>
    <div class="contact" style="left:16px;top:42px">427 Brisadores, Suite 392<br>Laredo, TX USA</div>
    <div class="ring" style="right:30px;bottom:18px;width:54px;height:54px;background:var(--blue);opacity:.08"></div>
  </section>

  <!-- Envelope, blue wave -->
  <section class="piece envelope-wave">
    <svg class="bg" viewBox="0 0 340 150" preserveAspectRatio="none"><path d="M0 0 L340 0 L340 40 C240 80 120 20 0 60Z" fill="var(--blue)"/><path d="M0 66 C120 26 240 86 340 46" stroke="var(--blue-dark)" stroke-width="2" fill="none"/></svg>
    <div class="ring" style="left:158px;top:12px;width:24px;height:24px;background:#fff"></div>
    <div class="contact" style="left:14px;top:80px">427 Brisadores, Suite 392<br>Laredo, TX USA</div>
    <div class="brand" style="left:14px;bottom:14px"><span class="dot"></span><span class="name">CASA<br>VANTORA</span></div>
    <div class="ring" style="right:24px;bottom:14px;width:50px;height:50px;background:var(--blue);opacity:.08"></div>
  </section>

</main>
</body>
</html>
```